MO&A - Business Card and Stationery for a Law Firm
Mendívil Ortuzar & Asociados
Professional
Julián Esteban Mendívil Ortuzar
Abogado
Carrera 48 No. 62-14 Of. 305
Bogotá D.C., Colombia
julian.mendivil@mendivilortuzar.com
www.mendivilortuzar.com
The text on the back of the card is in Spanish, for your information the meaning in English is as follows:
Companies in Colombia and abroad.
International business.
Tax planning.
Foreign investments.
Inmigration.
Industrial property.
Please distribute the text as you consider.
Logo and the following text:
Sociedades en Colombia y el exterior.
Negocios internacionales.
Planeación tributaria.
Inversión extranjera.
Asuntos migratorios.
Propiedad Industrial.

```html
<!DOCTYPE html>
<html lang="es">
<head>
<meta charset="utf-8">
<title>MO&amp;A — Tarjetas de presentación</title>
<link rel="stylesheet" href="https://fonts.googleapis.com/css2?family=Cinzel:wght@400;600&display=swap">
<style>
  :root {
    --navy: #142a52;
    --navy-deep: #10213f;
    --board: #e6e6e6;
    --paper: #ffffff;
    --stone: #a9a9a9;
    --ghost-light: rgba(20, 42, 82, 0.06);
    --ghost-dark: rgba(255, 255, 255, 0.07);
    --ghost-stone: rgba(255, 255, 255, 0.22);
  }
  * { box-sizing: border-box; margin: 0; padding: 0; }
  html, body {
    width: 1200px; height: 726px; overflow: hidden;
    background: var(--navy-deep);
    font-family: "Cinzel", "Trajan Pro", Georgia, serif;
  }
  .board {
    position: absolute; left: 24px; top: 24px;
    width: 1152px; height: 678px;
    background: var(--board);
  }
  .card {
    position: absolute; width: 505px; height: 289px;
    border-radius: 18px; overflow: hidden;
    border: 1.5px solid var(--navy);
  }
  .card--front { left: 48px; top: 43px; background: var(--paper); }
  .card--back-navy { left: 572px; top: 43px; background: var(--navy); border-color: var(--navy); }
  .card--back-white { left: 48px; top: 349px; background: var(--paper); }
  .card--back-stone { left: 572px; top: 349px; background: var(--stone); border-color: var(--stone); }

  .decor { position: absolute; width: 160px; height: 200px; }
  .card--back-navy .decor { right: 20px; top: 28px; background: var(--ghost-dark); }
  .card--back-white .decor { right: 0; top: 18px; background: var(--ghost-light); }
  .card--back-stone .decor { right: 16px; top: 18px; background: var(--ghost-stone); }

  .logo {
    position: absolute; display: flex; align-items: center; gap: 10px;
    font-weight: 600; font-size: 30px; letter-spacing: 1px; line-height: 1;
    color: var(--navy); white-space: nowrap;
  }
  .logo__square { width: 22px; height: 22px; background: currentColor; }
  .logo--light { color: var(--paper); }

  .front__logo { left: 14px; top: 18px; font-size: 21px; gap: 7px; letter-spacing: 0.5px; }
  .front__logo .logo__square { width: 16px; height: 16px; }
  .front__firm {
    position: absolute; left: 132px; top: 14px;
    color: var(--navy); font-size: 15px; line-height: 18px; letter-spacing: 0.3px;
    white-space: nowrap;
  }
  .front__name {
    position: absolute; left: 20px; width: 470px; top: 134px; text-align: center;
    color: var(--navy); font-size: 16px; font-weight: 400; letter-spacing: 0.3px;
    white-space: nowrap;
  }
  .front__role {
    position: absolute; left: 20px; width: 470px; top: 158px; text-align: center;
    color: var(--navy); font-size: 11px;
  }
  .front__contact {
    position: absolute; left: 19px; top: 206px;
    color: var(--navy); font-size: 10.5px; line-height: 14px; list-style: none;
    white-space: nowrap;
  }
  .front__tab {
    position: absolute; right: -2px; bottom: -2px; width: 80px; height: 104px;
    background: var(--navy); border-top-left-radius: 4px;
  }

  .services {
    position: absolute; list-style: none;
    font-size: 15.5px; line-height: 19px; letter-spacing: 0.2px;
  }
  .card--back-navy .logo { left: 46px; top: 38px; }
  .card--back-navy .services { left: 20px; top: 120px; color: var(--paper); }
  .card--back-white .logo,
  .card--back-stone .logo { left: 0; right: 0; justify-content: center; top: 58px; }
  .card--back-white .services,
  .card--back-stone .services { left: 0; right: 0; top: 160px; text-align: center; color: var(--navy); }
</style>
</head>
<body>
<main class="board">

  <section class="card card--front" aria-label="Frente de la tarjeta">
    <div class="logo front__logo"><span class="logo__square"></span>MO&amp;A</div>
    <p class="front__firm">Mendívil Ortuzar<br>&amp; Asociados</p>
    <h1 class="front__name">Julián Esteban Mendívil Ortuzar</h1>
    <p class="front__role">Abogado</p>
    <ul class="front__contact">
      <li>Carrera 48 No. 62-14 Of. 305</li>
      <li>Bogotá D.C., Colombia</li>
      <li>Cel: +57 3105550142 | Phone: +57 (1) 5550187</li>
      <li>Email: julian.mendivil@mendivilortuzar.com</li>
      <li>www.mendivilortuzar.com</li>
    </ul>
    <div class="front__tab"></div>
  </section>

  <section class="card card--back-navy" aria-label="Reverso azul">
    <div class="decor"></div>
    <div class="logo logo--light"><span class="logo__square"></span>MO&amp;A</div>
    <ul class="services">
      <li>Sociedades en Colombia y el exterior.</li>
      <li>Negocios internacionales.</li>
      <li>Planeación tributaria.</li>
      <li>Inversión extranjera.</li>
      <li>Asuntos migratorios.</li>
      <li>Propiedad Industrial.</li>
    </ul>
  </section>

  <section class="card card--back-white" aria-label="Reverso blanco">
    <div class="decor"></div>
    <div class="logo"><span class="logo__square"></span>MO&amp;A</div>
    <ul class="services">
      <li>Sociedades en Colombia y el exterior.</li>
      <li>Negocios internacionales.</li>
      <li>Planeación tributaria.</li>
      <li>Inversión extranjera.</li>
      <li>Asuntos migratorios.</li>
      <li>Propiedad Industrial.</li>
    </ul>
  </section>

  <section class="card card--back-stone" aria-label="Reverso gris">
    <div class="decor"></div>
    <div class="logo"><span class="logo__square"></span>MO&amp;A</div>
    <ul class="services">
      <li>Sociedades en Colombia y el exterior.</li>
      <li>Negocios internacionales.</li>
      <li>Planeación tributaria.</li>
      <li>Inversión extranjera.</li>
      <li>Asuntos migratorios.</li>
      <li>Propiedad Industrial.</li>
    </ul>
  </section>

</main>
</body>
</html>
```